Book Cover Quieting Gnats, Shouldn'ts and Maybes, Climbing out of the valley of sorrow

Need a book cover design for my new web site..Drpeterwalsby.com (website under construction) I'm appearing on Echo of Meridia radio show and want to add a cover design of my book.

My book with enpower people to break the chain of limiting beliefs and unlock their true potential so they will finally experience the life of their dreams

Radio

```html
<!DOCTYPE html>
<html lang="en">
<head>
<meta charset="utf-8">
<title>Quieting Gnats, Shouldn'ts and Maybes – Book Cover</title>
<link rel="stylesheet" href="https://fonts.googleapis.com/css2?family=Roboto:wght@100;700&display=swap">
<style>
  :root {
    --cover-teal: #6a9aa8;
    --cover-white: #ffffff;
  }
  html, body {
    margin: 0;
    padding: 0;
    overflow: hidden;
    background: var(--cover-teal);
  }
  .book-cover {
    position: relative;
    width: 800px;
    height: 1200px;
    background: var(--cover-teal);
    overflow: hidden;
    font-family: "Roboto", "Helvetica Neue", Arial, sans-serif;
    color: var(--cover-white);
  }
  .stripes {
    position: absolute;
    inset: 0;
  }
  .title {
    position: absolute;
    left: 133px;
    top: 262px;
    margin: 0;
    font-weight: 100;
    font-size: 60px;
    line-height: 64px;
    letter-spacing: -0.5px;
  }
  .title span { display: block; white-space: nowrap; }
  .subtitle {
    position: absolute;
    left: 138px;
    top: 408px;
    margin: 0;
    font-weight: 700;
    font-size: 22px;
    line-height: 26px;
    white-space: nowrap;
  }
  .author {
    position: absolute;
    left: 440px;
    top: 1011px;
    margin: 0;
    font-weight: 700;
    font-size: 24px;
    line-height: 28px;
    white-space: nowrap;
  }
</style>
</head>
<body>
  <main class="book-cover">
    <svg class="stripes" width="800" height="1200" viewBox="0 0 800 1200" aria-hidden="true">
      <g fill="var(--cover-white)">
        <!-- upper stripe group -->
        <rect x="139" y="0" width="9" height="256"/>
        <rect x="176" y="0" width="17" height="256"/>
        <rect x="215" y="46" width="4" height="210"/>
        <!-- lower stripe group -->
        <rect x="139" y="459" width="9" height="637"/>
        <rect x="176" y="459" width="17" height="741"/>
        <rect x="215" y="459" width="4" height="476"/>
      </g>
    </svg>

    <h1 class="title">
      <span>Quieting Gnats,</span>
      <span>Shouldn'ts and Maybes</span>
    </h1>
    <p class="subtitle">Climbing Out of the Valley of Sorrow</p>

    <p class="author">Dr. Peter Walsby</p>
  </main>
</body>
</html>
```